R&t Subterra

We specialize in CIPP pipe lining but do other underground utilities trenchless as well.

Target Market(s)

Trenchless sewer replacement

Contact Information for Business Card

Gavin Holtby 715-482-6130 Birchmoor rapids, mn

```html
<!DOCTYPE html>
<html lang="en">
<head>
<meta charset="utf-8">
<title>R&amp;t Subterra — Business Card</title>
<link rel="stylesheet" href="https://fonts.googleapis.com/css2?family=Arimo:wght@400;700&display=swap">
<style>
  :root {
    --bg: #d9d9db;
    --card: #f7f7f8;
    --brand-blue: #2f86c1;
    --brand-grey: #a9a9ab;
    --ink: #2b2b2b;
  }
  * { margin: 0; padding: 0; box-sizing: border-box; }
  html, body {
    width: 1200px; height: 800px; overflow: hidden;
    background: var(--bg);
    font-family: "Arimo", Arial, sans-serif;
  }
  .sheet {
    width: 1200px; height: 800px;
    display: flex; align-items: center; justify-content: center; gap: 40px;
  }
  .card {
    position: relative;
    width: 540px; height: 309px;
    background: var(--card);
    border-radius: 22px;
    overflow: hidden;
    box-shadow: 0 6px 18px rgba(0,0,0,0.18);
  }
  .card__swoosh { position: absolute; inset: 0; width: 100%; height: 100%; }
  .brand {
    display: flex; align-items: center; gap: 12px;
    color: var(--brand-blue); font-weight: 700;
    white-space: nowrap;
  }
  .brand__dot {
    border-radius: 50%; background: var(--brand-blue); flex: none;
  }
  .card--front .brand { position: absolute; left: 44px; top: 70px; font-size: 34px; }
  .card--front .brand__dot { width: 34px; height: 34px; }
  .contact { position: absolute; left: 44px; top: 160px; }
  .contact__name { color: var(--brand-blue); font-weight: 700; font-size: 24px; margin-bottom: 12px; }
  .contact__line { color: var(--ink); font-size: 17px; margin-bottom: 10px; display: flex; align-items: center; gap: 8px; white-space: nowrap; }
  .contact__icon { width: 14px; height: 14px; fill: var(--brand-blue); }
  .card--back { display: flex; align-items: center; justify-content: center; }
  .card--back .brand { font-size: 50px; gap: 18px; }
  .card--back .brand__dot { width: 52px; height: 52px; }
</style>
</head>
<body>
<main class="sheet">
  <section class="card card--front">
    <svg class="card__swoosh" viewBox="0 0 540 309" aria-hidden="true">
      <path d="M230 0 H540 V309 H510 C510 150 400 30 230 0 Z" fill="var(--brand-grey)"/>
      <path d="M350 10 C450 40 505 160 505 309 H540 V110 C480 50 420 20 350 10 Z" fill="var(--brand-blue)"/>
    </svg>
    <div class="brand"><span class="brand__dot"></span><span class="brand__name">R&amp;t Subterra</span></div>
    <div class="contact">
      <p class="contact__name">Gavin Holtby</p>
      <p class="contact__line">Birchmoor rapids, mn</p>
      <p class="contact__line">
        <svg class="contact__icon" viewBox="0 0 24 24" aria-hidden="true"><path d="M6.6 10.8a15 15 0 0 0 6.6 6.6l2.2-2.2a1 1 0 0 1 1-.25 11.4 11.4 0 0 0 3.6.57 1 1 0 0 1 1 1V20a1 1 0 0 1-1 1A17 17 0 0 1 3 4a1 1 0 0 1 1-1h3.5a1 1 0 0 1 1 1c0 1.25.2 2.450.57 3.57a1 1 0 0 1-.25 1z"/></svg>
        715-482-6130
      </p>
    </div>
  </section>
  <section class="card card--back">
    <div class="brand"><span class="brand__dot"></span><span class="brand__name">R&amp;t Subterra</span></div>
  </section>
</main>
</body>
</html>
```